Marlow Ridgeway a PlateWork Fabricator! Pressure Vessels, Stainless Vessels, Steel Fabricator!

Update and modernize the www.marlowridgeway.example website. Basically throwing away the old site and coming back with a new feel, new look, but some of the same content. One of our other companies is www.keltonbuilders.example and if you view that site you will get a idea of how we would like the site to feel. Below are the MR logos and the colors are #231F20 and #6D0B17 and the font is Ethnocentric Rg.

Target Market(s)

Steel Fabrication, Platework, Vessel Fabrication,

Industry/Entity Type

Steel

Coding

Coded - Design and coding required

Number of Pages Required

5+ page

Font styles to use
Other font styles liked:
• Ethnocentric Rg

Requirements
Must have
• Industry feel... site must flow and color scheme and font be consistent.

```html
<!DOCTYPE html>
<html lang="en">
<head>
<meta charset="utf-8">
<title>Marlow Ridgeway — Custom Steel Fabrication</title>
<link rel="stylesheet" href="https://fonts.googleapis.com/css2?family=Open+Sans:wght@400;600;700&family=Raleway:wght@600;700;800&display=swap">
<style>
:root{
  --ink:#231F20;
  --maroon:#6D0B17;
  --maroon-deep:#5a0912;
  --panel:#f2f2f2;
  --text:#3a3a3a;
  --white:#ffffff;
  --footer-bar:#141213;
}
*{margin:0;padding:0;box-sizing:border-box}
html,body{width:1200px;height:2889px;overflow:hidden;background:var(--white)}
body{position:relative;font-family:"Open Sans",Arial,sans-serif;color:var(--text)}
.abs{position:absolute}

/* header */
.brand{left:100px;top:36px;display:flex;align-items:center;gap:16px}
.brand-mark{width:78px;height:78px;border-radius:50%;border:6px solid var(--maroon)}
.brand-name{font-family:"Raleway",Arial,sans-serif;font-weight:800;color:var(--maroon);font-size:36px;line-height:36px;letter-spacing:1px;text-transform:uppercase}
.quote-btn{left:599px;top:58px;width:171px;height:40px;background:var(--maroon);color:var(--white);font-weight:600;font-size:16px;display:flex;align-items:center;justify-content:center}
.header-rule{left:824px;top:52px;width:1px;height:52px;background:#ddd}
.contact-line{left:866px;display:flex;align-items:center;gap:14px;font-size:16px;color:var(--ink)}
.contact-line svg{width:22px;height:18px;fill:var(--maroon)}

/* nav */
.main-nav{left:0;top:152px;width:1200px;height:43px;background:var(--ink)}
.main-nav span{position:absolute;top:0;line-height:43px;color:var(--white);font-weight:600;font-size:15px;transform:translateX(-50%);letter-spacing:.3px}
.main-nav svg{position:absolute;left:1033px;top:13px;width:17px;height:17px}

/* hero */
.hero{left:0;top:195px;width:1200px;height:518px;background:linear-gradient(180deg,#3d5a78 0%,#56667a 30%,#5e5352 60%,#3b3436 82%,#2a2729 100%)}
.hero-title{left:502px;top:330px;font-family:"Open Sans",Arial,sans-serif;font-weight:700;font-size:60px;line-height:70px;color:var(--white);letter-spacing:1px;white-space:nowrap}
.hero-sub{left:503px;top:422px;color:var(--white);font-size:29px;line-height:40px;text-transform:uppercase}
.hero-sub b{font-weight:700}
.product-select{left:505px;top:524px;width:327px;height:42px;border:2px solid var(--white);color:var(--white);font-size:15px;padding-left:16px;line-height:38px}
.product-select svg{position:absolute;right:14px;top:14px}
.dots{left:572px;top:646px;display:flex;gap:6px}
.dots i{width:11px;height:11px;border-radius:50%;border:2px solid var(--white)}
.dots i.on{background:var(--white)}

/* shared */
.panel{background:var(--panel)}
.section-title{font-family:"Raleway",Arial,sans-serif;font-weight:700;color:var(--ink);font-size:32px;line-height:43px}
.copy{font-size:14px;line-height:32px;color:#444}
.outline-btn{border:2px solid var(--maroon);color:var(--ink);font-weight:700;font-size:14px;display:flex;align-items:center;justify-content:center}
.bracket{fill:var(--ink)}

/* quality band */
.quality{left:0;top:1287px;width:1200px;height:489px;background:linear-gradient(90deg,var(--maroon-deep),var(--maroon) 40%,var(--maroon-deep))}
.quality h2{position:absolute;left:0;width:1200px;top:70px;text-align:center;font-family:"Raleway",Arial,sans-serif;font-weight:700;font-size:31px;color:var(--white)}
.quality p{position:absolute;left:160px;width:880px;top:128px;text-align:center;color:var(--white);font-size:14px;line-height:30px}
.badge{position:absolute;top:212px;height:110px;background:rgba(255,255,255,.88);border-radius:6px}
.arrow-ctrl{position:absolute;top:234px}
.band-btn{position:absolute;top:375px;height:36px;width:112px;font-weight:700;font-size:14px;display:flex;align-items:center;justify-content:center}
.band-btn.solid{background:var(--white);color:var(--ink);left:455px}
.band-btn.ghost{border:2px solid var(--white);color:var(--white);left:634px}

/* footer */
.footer{left:0;top:2427px;width:1200px;height:400px;background:var(--ink)}
.footer-brand{left:100px;top:2513px;display:flex;align-items:center;gap:16px}
.footer-brand .brand-mark{border-color:var(--white);width:100px;height:100px;border-width:7px}
.footer-brand .brand-name{color:var(--white);font-size:40px;line-height:42px}
.footer-label{color:var(--white);font-size:17px}
.social{top:2706px;width:38px;height:38px;border-radius:50%;background:var(--white)}
.signup{left:343px;top:2708px;width:268px;border-bottom:2px solid var(--white);color:var(--white);font-size:11px;padding-bottom:4px}
.signup svg{position:absolute;right:0;top:2px}
.quote-card{left:767px;top:2338px;width:385px;height:489px;background:var(--maroon)}
.quote-card h3{position:absolute;left:0;width:385px;top:40px;text-align:center;font-family:"Raleway",Arial,sans-serif;font-weight:700;font-size:31px;color:var(--white)}
.field{position:absolute;left:34px;width:316px;height:34px;background:var(--white);font-size:12px;color:#555;padding:8px 12px}
.submit{position:absolute;left:115px;top:407px;width:156px;height:36px;border:2px solid var(--white);color:var(--white);font-weight:700;font-size:14px;display:flex;align-items:center;justify-content:center}
.legal{left:0;top:2827px;width:1200px;height:62px;background:var(--footer-bar);color:#ddd;font-size:13px;text-align:center;line-height:62px}
</style>
</head>
<body>

<header>
  <div class="abs brand">
    <div class="brand-mark"></div>
    <div class="brand-name">Marlow<br>Ridgeway</div>
  </div>
  <div class="abs quote-btn">Request a Quote</div>
  <div class="abs header-rule"></div>
  <div class="abs contact-line" style="top:46px">
    <svg viewBox="0 0 22 16"><rect x="0" y="0" width="22" height="16" rx="2"/><path d="M1 2l10 7 10-7" stroke="#fff" stroke-width="1.6" fill="none"/></svg>
    <span>info@marlowridgeway.example</span>
  </div>
  <div class="abs contact-line" style="top:84px">
    <svg viewBox="0 0 20 20"><path d="M4 1l4 4-2 3c1 3 3 5 6 6l3-2 4 4-3 3C9 19 1 11 1 4z"/></svg>
    <span>Any Query : 555 - 010 - 1211</span>
  </div>
</header>

<nav class="abs main-nav">
  <span style="left:173px">HOME</span>
  <span style="left:273px">ABOUT</span>
  <span style="left:393px">PRODUCTS</span>
  <span style="left:520px">SERVICES</span>
  <span style="left:662px">WHO WE SERVE</span>
  <span style="left:817px">RESOURCES</span>
  <span style="left:946px">CONTACT</span>
  <svg viewBox="0 0 17 17"><circle cx="7" cy="7" r="5.5" fill="none" stroke="#fff" stroke-width="2.2"/><path d="M11 11l5 5" stroke="#fff" stroke-width="2.6"/></svg>
</nav>

<section>
  <div class="abs hero" role="img" aria-label="Welder at work in front of an industrial plant at dusk"></div>
  <h1 class="abs hero-title">MARLOW RIDGEWAY</h1>
  <p class="abs hero-sub">Your vision, our custom quality<br><b>Fabrication services</b></p>
  <div class="abs product-select">Select a Product
    <svg width="14" height="9" viewBox="0 0 14 9"><path d="M0 0h14L7 9z" fill="#fff"/></svg>
  </div>
  <div class="abs dots"><i class="on"></i><i></i><i></i><i></i></div>
</section>

<section>
  <div class="abs panel" style="left:447px;top:836px;width:705px;height:375px"></div>
  <svg class="abs" style="left:42px;top:767px" width="112" height="109" viewBox="0 0 112 109" role="img" aria-label="Steel corner bracket accent">
    <rect class="bracket" x="0" y="0" width="112" height="27"/><rect class="bracket" x="0" y="0" width="27" height="109"/>
  </svg>
  <svg class="abs" style="left:443px;top:1055px" width="114" height="110" viewBox="0 0 114 110" role="img" aria-label="Steel corner bracket accent">
    <rect class="bracket" x="87" y="0" width="27" height="110"/><rect class="bracket" x="0" y="83" width="114" height="27"/>
  </svg>
  <div class="abs" style="left:67px;top:792px;width:466px;height:350px;background:linear-gradient(135deg,#8a8478 0%,#6e5c46 50%,#b07a3e 75%,#4a3c30 100%)" role="img" aria-label="Worker grinding steel in a fabrication shop"></div>
  <h2 class="abs section-title" style="left:609px;top:875px">Success At Any Size</h2>
  <p class="abs copy" style="left:609px;top:938px;width:480px">We deliver fabrication solutions from small scale projects to our specialized oversized and overweight fabrication, processing, and handling capabilities. Steel fabricators proudly serving the power generation, water treatment, waste treatment, agriculture, chemical, food processing, mining, oil &amp; gas and heavy industry project sectors for nearly 40 years.</p>
  <div class="abs outline-btn" style="left:967px;top:1125px;width:133px;height:36px">Who We Serve</div>
</section>

<section class="abs quality">
  <h2>Quality Assurance Guaranteed</h2>
  <p>As experienced steel fabricators, we anticipate your needs and requirements from vision to production to delivery. Your steel fabrication products are manufactured by proven business processes and some of the industry’s top experts</p>
  <svg class="arrow-ctrl" style="left:42px" width="20" height="24" viewBox="0 0 20 24"><path d="M14 3L5 12l9 9" stroke="#fff" stroke-width="3.5" fill="none"/></svg>
  <div class="badge" style="left:160px;width:240px"></div>
  <div class="badge" style="left:500px;width:210px"></div>
  <div class="badge" style="left:820px;width:260px"></div>
  <svg class="arrow-ctrl" style="left:1142px" width="20" height="24" viewBox="0 0 20 24"><path d="M6 3l9 9-9 9" stroke="#fff" stroke-width="3.5" fill="none"/></svg>
  <div class="band-btn solid">Products</div>
  <div class="band-btn ghost">Services</div>
</section>

<section>
  <div class="abs panel" style="left:44px;top:1897px;width:674px;height:414px"></div>
  <h2 class="abs section-title" style="left:100px;top:1937px;width:520px">We May Not Be Superheroes But Our Customers Think We Are</h2>
  <p class="abs copy" style="left:100px;top:2032px;width:480px">We will keep Marlow-Ridgeway steel fabricators on our bidding list for vessels, tanks and stacks. Our catch tank constructed by them was of excellent workmanship and the exterior and interior met all of our expectations. We were impressed with the knowledgeable sales and engineering staff as well as their facilities. They worked well from the calculations for the foundation to the final tank design.</p>
  <div class="abs outline-btn" style="left:449px;top:2225px;width:150px;height:38px">Start Your Projects</div>
  <svg class="abs" style="left:639px;top:1828px" width="112" height="108" viewBox="0 0 112 108" role="img" aria-label="Steel corner bracket accent">
    <rect class="bracket" x="0" y="0" width="112" height="27"/><rect class="bracket" x="0" y="0" width="27" height="108"/>
  </svg>
  <svg class="abs" style="left:1040px;top:2119px" width="112" height="108" viewBox="0 0 112 108" role="img" aria-label="Steel corner bracket accent">
    <rect class="bracket" x="85" y="0" width="27" height="108"/><rect class="bracket" x="0" y="81" width="112" height="27"/>
  </svg>
  <div class="abs" style="left:664px;top:1853px;width:463px;height:349px;background:linear-gradient(160deg,#6f7882 0%,#8a5a3c 40%,#9a6240 60%,#3d6a9a 85%,#2c4f7a 100%)" role="img" aria-label="Welder working on a large steel cylinder on turning rolls"></div>
</section>

<footer>
  <div class="abs footer"></div>
  <div class="abs footer-brand">
    <div class="brand-mark"></div>
    <div class="brand-name">Marlow<br>Ridgeway</div>
  </div>
  <div class="abs footer-label" style="left:100px;top:2665px">Connect With Us :</div>
  <div class="abs social" style="left:98px"></div>
  <div class="abs social" style="left:147px"></div>
  <div class="abs social" style="left:193px"></div>
  <div class="abs footer-label" style="left:343px;top:2665px">Get In Touch</div>
  <div class="abs signup">Enter Your Email Here
    <svg width="18" height="10" viewBox="0 0 18 10"><path d="M0 5h16M12 1l4 4-4 4" stroke="#fff" stroke-width="2" fill="none"/></svg>
  </div>

  <div class="abs quote-card">
    <h3>Request A Quote</h3>
    <div class="field" style="top:104px">Name</div>
    <div class="field" style="top:152px">Email</div>
    <div class="field" style="top:202px">Phone no</div>
    <div class="field" style="top:251px">Company Name</div>
    <div class="field" style="top:299px;height:75px">Describe Your Project</div>
    <div class="submit">Submit Your Quote</div>
  </div>

  <div class="abs legal">© 2018 Marlow-Ridgeway. All Rights Reserved.</div>
</footer>

</body>
</html>
```